“Good Dog” fun and creative design sought for photo frame!

Seeking 8x10 inch photo frame with opening for dog’s photo. Dimensions must fit exact measurement specs of sample layout templates. Choose any of the three layout templates (labeled "Template 1," "Template 2" and "Template 3"). Our customers will upload their own dog’s photo to the frame and be able to print them out at 8 inches by 10 inches. The location of the opening for the dog’s photo must match one of the templates precisely. The opening for the dog's photo must have the EXACT same measurements as the templates - it cannot be round or any other shape - it must match the templates exactly. Samples of other Pawsome Snap Borders are posted just to give you a general idea of what some other designs look like from other designers. The text on the frame for this job should say “Good Dog.” Feel free to use the paw print PSD, but not required. Of course, no copyrighted materials should be used in the design.
Dog lovers
Seeking

```html
<!DOCTYPE html>
<html lang="en">
<head>
<meta charset="utf-8">
<title>Good Dog Photo Frame</title>
<link rel="stylesheet" href="https://fonts.googleapis.com/css2?family=Lobster&display=swap">
<style>
  :root {
    --backdrop: #e8e9eb;
    --wood-light: #a59b90;
    --wood-mid: #8f857b;
    --wood-dark: #7a7169;
    --plank-seam: rgba(60, 52, 45, 0.45);
    --photo-warm: #b4453a;
    --photo-dark: #1c1a1c;
    --ink-white: #ffffff;
  }
  * { margin: 0; padding: 0; box-sizing: border-box; }
  html, body {
    width: 1200px;
    height: 979px;
    overflow: hidden;
    background: var(--backdrop);
  }
  .frame-print {
    position: absolute;
    left: 150px;
    top: 114px;
    width: 901px;
    height: 721px;
    overflow: hidden;
  }
  .wood-backdrop {
    position: absolute;
    inset: 0;
    background: linear-gradient(180deg, var(--wood-mid) 0%, var(--wood-light) 35%, var(--wood-mid) 70%, var(--wood-dark) 100%);
  }
  .plank-seams {
    position: absolute;
    inset: 0;
  }
  .photo-mat {
    position: absolute;
    left: 44px;
    top: 172px;
    width: 428px;
    height: 346px;
    background: var(--ink-white);
    padding: 16px;
    box-shadow: 2px 3px 6px rgba(0, 0, 0, 0.35);
  }
  .photo-opening {
    width: 100%;
    height: 100%;
    background: linear-gradient(180deg, var(--photo-warm) 0%, #6b2d2c 30%, var(--photo-dark) 65%, var(--photo-dark) 100%);
  }
  .love-heart {
    position: absolute;
    left: 573px;
    top: 185px;
    width: 253px;
    height: 215px;
    filter: drop-shadow(2px 3px 3px rgba(0, 0, 0, 0.35));
  }
  .frame-title {
    position: absolute;
    left: 508px;
    top: 400px;
    width: 370px;
    font-family: "Lobster", cursive;
    font-size: 90px;
    line-height: 1.2;
    color: var(--ink-white);
    white-space: nowrap;
    text-shadow: 2px 3px 4px rgba(0, 0, 0, 0.4);
  }
  .paw-trail {
    position: absolute;
    left: 0;
    top: 595px;
    width: 901px;
    height: 95px;
    background: linear-gradient(180deg, rgba(255, 255, 255, 0.18), rgba(255, 255, 255, 0.28));
  }
</style>
</head>
<body>
  <main class="frame-print">
    <div class="wood-backdrop" role="img" aria-label="Weathered grey wooden plank background"></div>
    <svg class="plank-seams" viewBox="0 0 901 721" aria-hidden="true">
      <g stroke="var(--plank-seam)" stroke-width="3">
        <line x1="0" y1="78" x2="901" y2="78"/>
        <line x1="0" y1="192" x2="901" y2="192"/>
        <line x1="0" y1="305" x2="901" y2="305"/>
        <line x1="0" y1="418" x2="901" y2="418"/>
        <line x1="0" y1="530" x2="901" y2="530"/>
        <line x1="0" y1="650" x2="901" y2="650"/>
      </g>
    </svg>

    <div class="photo-mat">
      <div class="photo-opening" role="img" aria-label="Opening for the customer's dog photo"></div>
    </div>

    <svg class="love-heart" viewBox="0 0 253 215" aria-hidden="true">
      <path d="M126.5 206 L32 114 C-4 78 8 8 66 8 C96 8 116 28 126.5 48 C137 28 157 8 187 8 C245 8 257 78 221 114 Z"
            fill="none" stroke="var(--ink-white)" stroke-width="9" stroke-linejoin="round"/>
      <g fill="var(--ink-white)">
        <ellipse cx="126.5" cy="132" rx="20" ry="16"/>
        <ellipse cx="100" cy="108" rx="8" ry="11" transform="rotate(-25 100 108)"/>
        <ellipse cx="116" cy="93" rx="8" ry="11" transform="rotate(-8 116 93)"/>
        <ellipse cx="137" cy="93" rx="8" ry="11" transform="rotate(8 137 93)"/>
        <ellipse cx="153" cy="108" rx="8" ry="11" transform="rotate(25 153 108)"/>
      </g>
    </svg>

    <h1 class="frame-title">Good Dog</h1>

    <div class="paw-trail" role="img" aria-label="Row of white paw prints walking across the frame"></div>
  </main>
</body>
</html>
```